re-skin an existing app using new logo and color scheme

The company that created the existing app TotNest will be re-skinning the app on our behalf. We need to get a design submitted to them that retains the same functionality of their app but using our brand's look and feel. The product this app will be used in conjunction with is called Vero Band.
Vero Band is a stand-alone cellular watch that allows anyone from kids to seniors to make phone calls by simply pushing one of four buttons on the watch. The SOS button connects you to a live team of emergency professionals that can patch you to a 911 operator. Two of the other buttons are programmable to dial any desired phone number. The fourth button (called the "Magic" button) connects you with a live team of personal assistants that can help you with anything you want, including transferring you to any number, making dinner reservations, answering trivia, finding movie times and anything else you can imagine.
The built-in GPS functionality of the watch allows you to track the location of the watch at any time from the Vero Band website or the Vero Band app. You can also set up a perimeter around a specific area so that you can receive alerts when the watch travels outside of the "geofence".
Our slogan is: "Always safe on our watch"
We have included in the materials the Vero Band logo (in Adobe Illustrator). We have also included screen shots of some of the screens of the existing app (TotNest).
Using our logo, please design a re-skin of the attached screen shots. We want a simple, clean design. A great example of this is the Spot-o-Trek app:
https://www.portfoliyo.example/gallery/Spot-o-Trek/5927143
For the login redesign, this can be redone as far as the placement of the fields and buttons etc. Please make sure to include the slogan "Always safe on our watch" somewhere on the login screen.
For the navigation screen, only the top part will be available for you to redesign - the bottom 80% of the screen needs to stay the same. (where it says "Device name: Teal Band" and below)
For the privilege screen, this can be completely redesigned.
For the family numbers setting screen, this can be completely redesigned.
For the whitelist setting screen, this can be completely redesigned.
Any questions, let us know.

```html
<!DOCTYPE html>
<html lang="en">
<head>
<meta charset="utf-8">
<title>Vero Band – app screens</title>
<link rel="stylesheet" href="https://fonts.googleapis.com/css2?family=Lato:wght@300;400;700&display=swap">
<style>
:root{
  --cyan:#5dd3ec;
  --teal:#1f6b74;
  --teal-deep:#1a5a62;
  --ink:#3a3a3a;
  --ink-soft:#555;
  --status:#222;
  --line:#e2e2e2;
  --paper:#fff;
}
*{box-sizing:border-box;margin:0;padding:0}
html,body{width:1200px;height:1200px;overflow:hidden}
body{background:linear-gradient(180deg,#f1f1f1,#e2e2e2);font-family:"Lato",sans-serif;color:var(--ink);position:relative}
.screen{position:absolute;width:286px;height:508px;background:var(--paper);overflow:hidden;box-shadow:0 6px 14px rgba(0,0,0,.18)}
.screen *{position:absolute}
.status{left:0;top:0;width:100%;height:20px;background:var(--status);color:#fff;font-size:12px;line-height:20px}
.status .carrier{left:6px;top:0}
.status .level{right:6px;top:0;display:flex;align-items:center;gap:4px}
.status svg{position:static}
.strip{left:0;width:100%;background:var(--cyan)}
.center{left:0;width:100%;text-align:center}
.brand{color:#fff;font-weight:400;letter-spacing:.3px}

/* profile */
.profile-head{left:0;top:27px;width:100%;height:153px;background:var(--teal)}
.avatar{left:91px;top:130px;width:104px;height:104px;border-radius:50%;background:radial-gradient(circle at 50% 40%,#c9c9c9,#7a7a7a)}
.email{top:245px;font-size:14px;font-weight:300}
.menu{left:0;top:266px;width:100%;height:199px;border-top:1px solid var(--line)}
.menu .cell{width:143px;height:99px;border-bottom:1px solid var(--line)}
.menu .cell span{left:0;width:100%;text-align:center;top:38px;font-size:17px;font-weight:300;line-height:20px;color:var(--ink-soft)}
.menu .cell svg{left:8px;top:8px}
.menu .vsplit{left:142px;top:0;width:1px;height:199px;background:var(--line)}
.logout{left:0;top:465px;width:100%;height:43px;background:var(--cyan);color:#fff;text-align:center;line-height:43px;font-size:18px;font-weight:300}

/* login */
.login-bg{left:0;top:20px;width:100%;height:488px;background:linear-gradient(180deg,#2d6870 0%,#1d5f68 45%,#235f63 100%)}
.slogan{font-size:28px;font-weight:300;line-height:30px;color:#fff}
.slogan b{position:static;color:var(--cyan);font-weight:300}
.field{left:38px;width:208px;height:23px;border:1px solid rgba(255,255,255,.8);border-radius:2px;color:#fff;font-size:13px;text-align:center;line-height:21px}
.remember{left:80px;top:378px;font-size:9px;color:#fff;display:flex;align-items:center;gap:4px}
.remember i{position:static;width:8px;height:8px;border:1px solid #fff}
.go{left:109px;top:406px;width:60px;height:25px;border:1px solid #fff;border-radius:3px;color:#fff;text-align:center;line-height:23px;font-size:16px;font-weight:300}
.register{left:178px;top:410px;color:#fff;font-size:13px}

/* sub headers */
.back{width:40px;height:40px;border-radius:50%;background:var(--cyan);left:15px;top:24px;border:2px solid #fff}
.back svg{left:10px;top:10px}
.title{font-size:21px;font-weight:400;line-height:21px;color:var(--ink)}
.rule{left:0;width:100%;height:1px;background:var(--line)}

/* location */
.device{left:0;top:112px;width:100%;height:32px;border-top:1px solid var(--line);font-size:11px;line-height:31px}
.map{left:0;top:144px;width:100%;height:278px;background:linear-gradient(135deg,#dcd8d0 0%,#e6e2da 40%,#cfe0c4 60%,#e4e0d8 80%,#8fb8e6 100%)}
.map-pin{left:150px;top:225px}
.map-bar{left:0;top:422px;width:100%;height:28px;background:var(--teal-deep);color:#fff;font-size:13px;line-height:28px}
.num{width:20px;height:20px;border-radius:50%;text-align:center;line-height:20px;font-size:13px}
.tabs{left:0;top:450px;width:100%;height:58px;background:var(--cyan);display:flex}
.tabs div{position:relative;flex:1;border-right:1px solid rgba(255,255,255,.35);color:#fff;font-size:13px;font-weight:300;text-align:center}
.tabs div:last-child{border-right:0}
.tabs svg{left:50%;margin-left:-9px;top:8px}
.tabs span{left:0;width:100%;top:29px}

/* whitelist */
.row-label{left:47px;font-size:17px;font-weight:300;color:var(--ink-soft)}
.row-value{left:150px;font-size:16px;font-weight:400;color:var(--ink)}
.badge{left:13px;width:24px;height:24px;border-radius:50%;background:var(--cyan);color:#fff;font-size:13px;text-align:center;line-height:24px}
.btn{background:var(--cyan);color:#fff;text-align:center;font-weight:300;border-radius:2px}
.bottom-line{left:0;top:503px;width:100%;height:5px;background:var(--cyan)}
.fam-label{font-size:17px;font-weight:300;color:var(--ink-soft)}
.fam-num{font-size:19px;color:var(--ink)}
</style>
</head>
<body>

<!-- Profile -->
<section class="screen" style="left:118px;top:92px">
  <div class="status"><span class="carrier">●●●●○ KORA</span><span class="level">82% <svg width="22" height="10"><rect x="0.5" y="0.5" width="18" height="9" fill="none" stroke="#fff"/><rect x="2" y="2" width="15" height="6" fill="#fff"/><rect x="19" y="3" width="2" height="4" fill="#fff"/></svg></span></div>
  <div class="strip" style="top:20px;height:7px"></div>
  <div class="profile-head" role="img" aria-label="Faint city map texture in teal"></div>
  <div class="strip" style="top:180px;height:6px"></div>
  <div class="center brand" style="top:80px;font-size:15px">Vero Band</div>
  <div class="avatar" role="img" aria-label="Profile photo of the account holder"></div>
  <div class="center email">adam@mailnest.example</div>
  <div class="menu">
    <div class="cell" style="left:0;top:0">
      <svg width="20" height="24" viewBox="0 0 20 24"><path d="M10 23s8-8 8-13a8 8 0 0 0-16 0c0 5 8 13 8 13z" fill="none" stroke="var(--cyan)" stroke-width="1.3"/><circle cx="10" cy="10" r="3" fill="none" stroke="var(--cyan)" stroke-width="1.3"/></svg>
      <span>Location<br>service</span></div>
    <div class="cell" style="left:143px;top:0">
      <svg width="26" height="22" viewBox="0 0 26 22"><path d="M13 2c6 0 11 3.5 11 8s-5 8-11 8l-6 3 1-4c-3-1.5-6-4-6-7 0-4.5 5-8 11-8z" fill="none" stroke="var(--cyan)" stroke-width="1.3"/><path d="M8 8h10M8 12h8" stroke="var(--cyan)" stroke-width="1.2"/></svg>
      <span>Alarm<br>messages</span></div>
    <div class="cell" style="left:0;top:99px">
      <svg width="24" height="24" viewBox="0 0 24 24"><path d="M4 8a10 10 0 1 1-1 6" fill="none" stroke="var(--cyan)" stroke-width="1.3"/><path d="M2 4v5h5" fill="none" stroke="var(--cyan)" stroke-width="1.3"/><path d="M13 7v6l4 2" fill="none" stroke="var(--cyan)" stroke-width="1.3"/></svg>
      <span>Device<br>management</span></div>
    <div class="cell" style="left:143px;top:99px">
      <svg width="20" height="26" viewBox="0 0 20 26"><rect x="2" y="2" width="16" height="22" fill="none" stroke="var(--cyan)" stroke-width="1.3"/><path d="M2 6h16M10 11v8M6 15h8" stroke="var(--cyan)" stroke-width="1.2"/></svg>
      <span>System<br>help</span></div>
    <div class="vsplit"></div>
  </div>
  <div class="logout">Logout</div>
</section>

<!-- Login -->
<section class="screen" style="left:458px;top:61px">
  <div class="status"><span class="carrier">●●●●○ KORA</span><span class="level">82% <svg width="22" height="10"><rect x="0.5" y="0.5" width="18" height="9" fill="none" stroke="#fff"/><rect x="2" y="2" width="15" height="6" fill="#fff"/><rect x="19" y="3" width="2" height="4" fill="#fff"/></svg></span></div>
  <div class="login-bg" role="img" aria-label="Parent and child walking on a tree-lined path, tinted teal"></div>
  <div class="center brand" style="top:114px;font-size:20px">Vero Band</div>
  <div class="center slogan" style="top:188px"><b>Always safe</b><br>on our watch</div>
  <div class="center" style="top:283px;color:#fff;font-size:18px">Login</div>
  <div class="field" style="top:316px">username</div>
  <div class="field" style="top:350px">password</div>
  <div class="remember"><i></i>Remember password</div>
  <div class="go">Go</div>
  <div class="register">or Register</div>
  <div class="bottom-line"></div>
</section>

<!-- Location -->
<section class="screen" style="left:798px;top:92px">
  <div class="status"><span class="carrier">●●●●○ KORA</span><span class="level">82% <svg width="22" height="10"><rect x="0.5" y="0.5" width="18" height="9" fill="none" stroke="#fff"/><rect x="2" y="2" width="15" height="6" fill="#fff"/><rect x="19" y="3" width="2" height="4" fill="#fff"/></svg></span></div>
  <div class="strip" style="top:20px;height:22px"></div>
  <div class="back"><svg width="16" height="16"><path d="M12 2 4 8l8 6" fill="none" stroke="#fff" stroke-width="2.5"/></svg></div>
  <svg style="left:83px;top:42px" width="20" height="24" viewBox="0 0 20 24"><path d="M10 23s8-8 8-13a8 8 0 0 0-16 0c0 5 8 13 8 13z" fill="#fff" stroke="var(--cyan)" stroke-width="1.3"/><circle cx="10" cy="10" r="3" fill="none" stroke="var(--cyan)" stroke-width="1.3"/></svg>
  <div class="center title" style="top:64px">Location<br>service</div>
  <div class="device"><span style="left:8px">Device name: Teal Band</span>
    <svg style="left:192px;top:11px" width="18" height="10"><rect x="0.5" y="0.5" width="15" height="9" fill="none" stroke="var(--cyan)"/><path d="M3 3v4M6 3v4M9 3v4" stroke="var(--cyan)"/><rect x="16" y="3" width="2" height="4" fill="var(--cyan)"/></svg>
    <svg style="left:222px;top:9px" width="10" height="13" viewBox="0 0 20 24"><path d="M10 23s8-8 8-13a8 8 0 0 0-16 0c0 5 8 13 8 13z" fill="none" stroke="var(--cyan)" stroke-width="2"/></svg>
    <span style="left:241px">Offline</span></div>
  <div class="map" role="img" aria-label="Street map around the watch location"></div>
  <svg class="map-pin" width="32" height="40" viewBox="0 0 32 40"><path d="M16 39s14-13 14-23a14 14 0 0 0-28 0c0 10 14 23 14 23z" fill="var(--cyan)"/><text x="16" y="22" text-anchor="middle" fill="#fff" font-family="Lato,sans-serif" font-size="16">1</text></svg>
  <div class="map-bar"><span class="num" style="left:19px;top:4px;background:#fff;color:var(--teal-deep)">1</span><span style="left:44px">Teal</span></div>
  <div class="tabs">
    <div><svg width="18" height="18"><circle cx="9" cy="9" r="7.5" fill="none" stroke="#fff" stroke-width="1.3"/><path d="M9 4v5l3 2" fill="none" stroke="#fff" stroke-width="1.3"/></svg><span>History</span></div>
    <div><svg width="18" height="18"><rect x="3" y="2" width="12" height="15" fill="none" stroke="#fff" stroke-width="1.3"/><path d="M6 6h6M6 9h6M6 12h6" stroke="#fff"/></svg><span>Tracking</span></div>
    <div><svg width="18" height="18"><path d="M9 12s5-4 5-7a5 5 0 0 0-10 0c0 3 5 7 5 7z" fill="none" stroke="#fff" stroke-width="1.3"/><path d="M2 11v6h14v-6" fill="none" stroke="#fff" stroke-width="1.3"/></svg><span>Geofence</span></div>
    <div><svg width="18" height="18"><circle cx="9" cy="9" r="3" fill="none" stroke="#fff" stroke-width="1.3"/><circle cx="9" cy="9" r="7" fill="none" stroke="#fff" stroke-width="1.3" stroke-dasharray="3 2"/></svg><span>Setting</span></div>
  </div>
</section>

<!-- Whitelist -->
<section class="screen" style="left:261px;top:646px">
  <div class="status"><span class="carrier">●●●●○ KORA</span><span class="level">82% <svg width="22" height="10"><rect x="0.5" y="0.5" width="18" height="9" fill="none" stroke="#fff"/><rect x="2" y="2" width="15" height="6" fill="#fff"/><rect x="19" y="3" width="2" height="4" fill="#fff"/></svg></span></div>
  <div class="strip" style="top:20px;height:22px"></div>
  <div class="back"><svg width="16" height="16"><path d="M12 2 4 8l8 6" fill="none" stroke="#fff" stroke-width="2.5"/></svg></div>
  <svg style="left:74px;top:42px" width="34" height="28" viewBox="0 0 34 28"><path d="M2 8c0-5 30-5 30 0v3h-7V7H9v4H2z" fill="#fff" stroke="var(--cyan)" stroke-width="1.3"/><g fill="var(--cyan)"><rect x="9" y="14" width="3" height="3"/><rect x="15" y="14" width="3" height="3"/><rect x="21" y="14" width="3" height="3"/><rect x="9" y="19" width="3" height="3"/><rect x="15" y="19" width="3" height="3"/><rect x="21" y="19" width="3" height="3"/><rect x="9" y="24" width="3" height="3"/><rect x="15" y="24" width="3" height="3"/><rect x="21" y="24" width="3" height="3"/></g></svg>
  <div class="center title" style="top:63px">Whitelist<br>setting</div>
  <div class="rule" style="top:113px"></div>

  <div class="rule" style="top:146px"></div><div class="rule" style="top:171px"></div><div class="rule" style="top:194px"></div>
  <div class="badge" style="top:158px">1</div>
  <div class="row-label" style="top:148px">Name 1</div><div class="row-value" style="top:149px">Adam</div>
  <div class="row-label" style="top:172px">Number 1</div><div class="row-value" style="top:173px">80 15 32 90 61</div>

  <div class="rule" style="top:215px"></div><div class="rule" style="top:241px"></div><div class="rule" style="top:263px"></div>
  <div class="badge" style="top:228px">2</div>
  <div class="row-label" style="top:218px">Name 2</div><div class="row-value" style="top:219px">Michael</div>
  <div class="row-label" style="top:242px">Number 2</div><div class="row-value" style="top:243px">80 15 32 90 61</div>

  <div class="rule" style="top:285px"></div><div class="rule" style="top:310px"></div><div class="rule" style="top:333px"></div>
  <div class="badge" style="top:297px">3</div>
  <div class="row-label" style="top:287px">Name 3</div><div class="row-value" style="top:288px">Anna</div>
  <div class="row-label" style="top:311px">Number 3</div><div class="row-value" style="top:312px">80 15 32 90 61</div>

  <div class="rule" style="top:354px"></div><div class="rule" style="top:380px"></div><div class="rule" style="top:402px"></div>
  <div class="badge" style="top:367px">4</div>
  <div class="row-label" style="top:357px">Name 4</div><div class="row-value" style="top:358px">April</div>
  <div class="row-label" style="top:381px">Number 4</div><div class="row-value" style="top:382px">80 15 32 90 61</div>

  <div class="btn" style="left:103px;top:438px;width:82px;height:25px;line-height:25px;font-size:19px">Submit</div>
  <div class="bottom-line"></div>
</section>

<!-- Family numbers -->
<section class="screen" style="left:655px;top:646px">
  <div class="status"><span class="carrier">●●●●○ KORA</span><span class="level">82% <svg width="22" height="10"><rect x="0.5" y="0.5" width="18" height="9" fill="none" stroke="#fff"/><rect x="2" y="2" width="15" height="6" fill="#fff"/><rect x="19" y="3" width="2" height="4" fill="#fff"/></svg></span></div>
  <div class="strip" style="top:20px;height:22px"></div>
  <div class="back"><svg width="16" height="16"><path d="M12 2 4 8l8 6" fill="none" stroke="#fff" stroke-width="2.5"/></svg></div>
  <svg style="left:74px;top:42px" width="34" height="28" viewBox="0 0 34 28"><path d="M2 8c0-5 30-5 30 0v3h-7V7H9v4H2z" fill="#fff" stroke="var(--cyan)" stroke-width="1.3"/><g fill="var(--cyan)"><rect x="9" y="14" width="3" height="3"/><rect x="15" y="14" width="3" height="3"/><rect x="21" y="14" width="3" height="3"/><rect x="9" y="19" width="3" height="3"/><rect x="15" y="19" width="3" height="3"/><rect x="21" y="19" width="3" height="3"/><rect x="9" y="24" width="3" height="3"/><rect x="15" y="24" width="3" height="3"/><rect x="21" y="24" width="3" height="3"/></g></svg>
  <div class="center title" style="top:63px">Family<br>numbers setting</div>
  <div class="rule" style="top:113px"></div>
  <div class="btn" style="left:51px;top:142px;width:183px;height:26px;line-height:26px;font-size:19px">Get family number</div>

  <div class="center fam-label" style="top:193px">Number 1</div>
  <div class="rule" style="top:218px"></div>
  <div class="center fam-num" style="top:221px">80 15 32 90 61</div>
  <div class="rule" style="top:248px"></div>

  <div class="center fam-label" style="top:280px">Number 2</div>
  <div class="rule" style="top:303px"></div>
  <div class="center fam-num" style="top:306px">56 48 21 73 09</div>
  <div class="rule" style="top:333px"></div>

  <div class="center fam-label" style="top:360px">Number 3</div>
  <div class="rule" style="top:385px"></div>
  <div class="center fam-num" style="top:388px">36 72 05 18 44</div>
  <div class="rule" style="top:414px"></div>

  <div class="btn" style="left:102px;top:446px;width:81px;height:25px;line-height:25px;font-size:19px">Submit</div>
  <div class="bottom-line"></div>
</section>

</body>
</html>
```